Webbanner-Design für Online Pfandhaus
Zielgruppe
Online Pfandhaus
Aufgabenstellung
Der Banner für unsere Webseite soll neu gestaltet werden. (Siehe Bilddatei)
Ziel ist es einen schönen, konvertierenden Banner zu gestalten. Der Banner soll sich an die Seite anpassen.
Der Banner wird dann auch für Social Media benötigt.

```html
<!DOCTYPE html>
<html lang="de">
<head>
<meta charset="utf-8">
<title>Online-Pfandhaus Banner</title>
<link rel="stylesheet" href="https://fonts.googleapis.com/css2?family=Oswald:wght@500&family=Poppins:wght@400;700&family=Open+Sans:ital,wght@0,600;1,700&display=swap">
<style>
:root{
  --navy:#2b3a8f;
  --ink:#2b2b2b;
  --hero-top:#e4ebf3;
  --hero-bottom:#cfdceb;
  --green-a:#10cf6c;
  --green-b:#0a9447;
  --orange-a:#f7a21e;
  --orange-b:#f08a10;
  --white:#ffffff;
}
*{margin:0;padding:0;box-sizing:border-box}
html,body{width:1200px;height:442px;overflow:hidden;background:var(--white)}
.banner{position:relative;width:1200px;height:442px;overflow:hidden}
.site-header{position:absolute;left:0;top:0;width:1200px;height:54px;background:var(--white);border-bottom:1px solid #e3e7ee;z-index:3}
.brand{position:absolute;left:224px;top:14px;display:flex;align-items:center;gap:6px;font-family:'Poppins',sans-serif;font-weight:700;font-size:14px;color:var(--navy)}
.brand-dot{width:22px;height:22px;border-radius:50%;background:var(--navy)}
.main-nav a{position:absolute;top:17px;font-family:'Oswald',sans-serif;font-weight:500;font-size:13.5px;color:var(--navy);text-decoration:none;white-space:nowrap}
.hero{position:absolute;left:0;top:54px;width:1200px;height:388px;background:linear-gradient(160deg,var(--hero-top),var(--hero-bottom))}
.hero-photo{position:absolute;left:0;top:0}
.eyebrow{position:absolute;left:224px;top:78px;font-family:'Poppins',sans-serif;font-size:11px;letter-spacing:1.2px;color:var(--navy)}
.headline{position:absolute;left:224px;top:100px;font-family:'Poppins',sans-serif;font-weight:700;font-size:29px;line-height:34px;color:var(--ink)}
.lead{position:absolute;left:224px;top:183px;font-family:'Poppins',sans-serif;font-size:15px;line-height:22px;color:var(--ink)}
.lead strong{font-weight:700}
.cta{position:absolute;left:224px;top:271px;width:194px;height:40px;border-radius:3px;background:linear-gradient(90deg,var(--green-a),var(--green-b));display:flex;align-items:center;justify-content:space-between;padding:0 14px 0 19px;font-family:'Open Sans',sans-serif;font-weight:600;font-size:11px;color:var(--white);text-decoration:none}
.item{position:absolute;border-radius:50%;background:var(--white);border:2.5px solid var(--orange-b)}
.item-shot{position:absolute;left:22%;top:15%;width:56%;height:70%;border-radius:10px;background:linear-gradient(160deg,#cfd3d8,#4a4d52)}
.price{position:absolute;width:82px;height:34px}
.price::before{content:"";position:absolute;inset:0;border-radius:8px;background:linear-gradient(90deg,var(--orange-b),var(--orange-a));transform:skewX(-18deg)}
.price span{position:relative;display:block;text-align:center;line-height:34px;font-family:'Open Sans',sans-serif;font-style:italic;font-weight:700;font-size:18px;color:var(--white)}
</style>
</head>
<body>
<div class="banner">
  <header class="site-header">
    <div class="brand"><span class="brand-dot"></span>leihWerk.de</div>
    <nav class="main-nav">
      <a style="left:464px">Start</a>
      <a style="left:514px">Anfrage</a>
      <a style="left:576px">Ablauf</a>
      <a style="left:632px">Standorte ⌄</a>
      <a style="left:719px">Wissenswertes</a>
      <a style="left:815px">FAQ</a>
      <a style="left:858px">Kontakt</a>
      <a style="left:922px">Über uns</a>
    </nav>
  </header>
  <section class="hero">
    <svg class="hero-photo" width="1200" height="388" viewBox="0 0 1200 388" role="img" aria-label="Foto: entspannter junger Mann auf dem Sofa, Hände hinter dem Kopf">
      <defs>
        <linearGradient id="photoTone" x1="0" y1="0" x2="0.3" y2="1">
          <stop offset="0" stop-color="#d9a98e"/>
          <stop offset="0.4" stop-color="#c99c88"/>
          <stop offset="0.6" stop-color="#4d5f86"/>
          <stop offset="1" stop-color="#2e3d5e"/>
        </linearGradient>
      </defs>
      <path d="M620 0 H1200 V64 C1188 76 1170 88 1150 97 L802 277 L698 212 L627 38 C621 22 616 8 620 0 Z" fill="url(#photoTone)"/>
    </svg>
    <p class="eyebrow">ONLINE-PFANDHAUS</p>
    <h1 class="headline">Genießen Sie<br>Ihre Freiheit</h1>
    <p class="lead">Beleihen Sie jetzt Ihre Wertgegenstände und<br>erhalten Sie in kürzester Zeit Ihr Geld.<br><strong>100% sicher &amp; diskret.</strong></p>
    <a class="cta" href="#">Jetzt Angebot erhalten
      <svg width="20" height="16" viewBox="0 0 20 16" fill="none" stroke="#fff" stroke-width="2"><path d="M1 8H18M11 1l7 7-7 7"/></svg>
    </a>
    <div class="item" style="left:617px;top:216px;width:143px;height:143px"><div class="item-shot" role="img" aria-label="Produktfoto Smartphone"></div></div>
    <div class="item" style="left:802px;top:222px;width:134px;height:134px"><div class="item-shot" role="img" aria-label="Produktfoto Armbanduhr"></div></div>
    <div class="item" style="left:972px;top:214px;width:142px;height:142px"><div class="item-shot" role="img" aria-label="Produktfoto Spiegelreflexkamera"></div></div>
    <div class="price" style="left:696px;top:310px"><span>362 €</span></div>
    <div class="price" style="left:879px;top:310px"><span>335 €</span></div>
    <div class="price" style="left:1049px;top:310px"><span>728 €</span></div>
  </section>
</div>
</body>
</html>
```